Velcrest-Aura

Letter heads, business cards, packaging envelopes big and small, and stationery
We have logo design and trademarked approval, we would lie to
upload design to help create this project.
This product was created for my Mother a 4 time diganosed Cancer
Survivor, This product has patent pending and now will be offered to the general public as well.
We are looking foward to working with all of you as this product
and stationary will be viewed worldwide.
Thanks
The Kindale Family

Target Market(s)

all ages and worldwide

Industry/Entity Type

Business

Requirements
Must have
• Our Logo

```html
<!DOCTYPE html>
<html lang="en">
<head>
<meta charset="utf-8">
<title>Velcrest-Aura Stationery</title>
<link rel="stylesheet" href="https://fonts.googleapis.com/css2?family=Arimo:wght@400;700&display=swap">
<style>
  :root {
    --navy: #1f3868;
    --red: #c0202a;
    --paper: #ffffff;
    --backdrop: #666666;
    --edge: #b9b9b9;
  }
  * { box-sizing: border-box; margin: 0; padding: 0; }
  html, body { width: 1200px; height: 985px; overflow: hidden; }
  body {
    position: relative;
    background: var(--backdrop);
    font-family: "Arimo", Arial, sans-serif;
    color: var(--navy);
  }
  .sheet {
    position: absolute;
    background: var(--paper);
    border: 1px solid var(--edge);
    overflow: hidden;
  }
  .flap { position: absolute; left: 0; top: 0; width: 100%; display: block; }
  .flap-content {
    position: absolute; left: 0; width: 100%;
    text-align: center; color: var(--paper);
  }
  .flap-content.on-white { color: var(--red); }
  .wave { position: absolute; left: 0; bottom: 0; width: 100%; display: block; }

  .mark {
    display: inline-flex; align-items: center; gap: 5px;
    font-weight: 700; color: var(--navy); white-space: nowrap; letter-spacing: -0.2px;
  }
  .mark-dot {
    display: inline-block; border-radius: 50%; background: var(--red); flex: none;
  }
  .flap-content .mark { color: inherit; font-size: 13px; }
  .flap-content .mark-dot { width: 9px; height: 9px; background: currentColor; }
  .flap-url { display: block; font-size: 5px; margin-top: 4px; }

  .tagline { font-weight: 700; color: var(--navy); white-space: nowrap; }
  .address { color: var(--navy); white-space: nowrap; }
  .web { position: absolute; color: var(--paper); font-weight: 700; white-space: nowrap; }

  /* large envelopes */
  .env-large { width: 408px; }
  .env-white { left: 96px; top: 52px; height: 559px; }
  .env-red { left: 78px; top: 134px; height: 640px; }
  .env-blue { left: 78px; top: 216px; height: 558px; }

  /* letterhead */
  .letterhead { left: 34px; top: 299px; width: 409px; height: 559px; }
  .letterhead-head { position: absolute; top: 20px; left: 0; width: 100%; text-align: center; }
  .letterhead-head .mark { font-size: 15px; }
  .letterhead-head .mark-dot { width: 11px; height: 11px; }
  .letterhead-head .tagline { font-size: 6px; margin-top: 1px; }
  .letterhead-head .address { font-size: 7.5px; margin-top: 6px; }
  .letterhead .web { left: 68px; bottom: 14px; font-size: 6.5px; font-weight: 400; }

  /* business cards */
  .card { width: 317px; height: 181px; }
  .card-front { left: 570px; top: 26px; }
  .card-back { left: 836px; top: 260px; }
  .card-name { position: absolute; top: 22px; left: 0; width: 100%; text-align: center; font-size: 11px; font-weight: 700; color: var(--navy); }
  .card-name .role { font-size: 9px; font-weight: 400; }
  .card-front .brand { position: absolute; left: 14px; top: 70px; }
  .card-front .mark { font-size: 18px; }
  .card-front .mark-dot { width: 13px; height: 13px; }
  .card-front .tagline { font-size: 8px; padding-left: 18px; margin-top: 1px; }
  .contacts { position: absolute; left: 213px; top: 56px; list-style: none; font-size: 7.5px; color: var(--navy); line-height: 10.5px; }
  .contacts li { display: flex; align-items: center; gap: 3px; white-space: nowrap; }
  .contacts svg { width: 7px; height: 7px; fill: var(--navy); flex: none; }
  .card-front .web { right: 14px; bottom: 10px; font-size: 8px; font-weight: 400; line-height: 11px; width: 100px; white-space: normal; }
  .card-back .brand { position: absolute; left: 38px; top: 46px; }
  .card-back .mark { font-size: 25px; }
  .card-back .mark-dot { width: 17px; height: 17px; }
  .card-back .tagline { font-size: 11px; padding-left: 22px; margin-top: 1px; }
  .card-back .web { right: 16px; bottom: 12px; font-size: 9px; }

  /* regular envelopes */
  .env-regular-back { left: 599px; top: 509px; width: 571px; height: 255px; }
  .env-regular-front { left: 551px; top: 664px; width: 572px; height: 254px; }
  .env-regular-back .mark { font-size: 15px; }
  .env-regular-back .mark-dot { width: 11px; height: 11px; }
  .env-regular-front .brand { position: absolute; left: 15px; top: 26px; }
  .env-regular-front .mark { font-size: 17px; }
  .env-regular-front .mark-dot { width: 12px; height: 12px; }
  .env-regular-front .tagline { font-size: 7.5px; padding-left: 17px; }
  .env-regular-front .address { font-size: 8.5px; margin-top: 7px; }
  .env-regular-front .web { left: 92px; bottom: 12px; font-size: 9px; font-weight: 400; }

  .caption { position: absolute; color: #ffffff; white-space: nowrap; transform: translateX(-50%); }
  .caption-large-env { left: 240px; top: 862px; font-size: 11px; }
  .caption-bc-front { left: 721px; top: 208px; font-size: 20px; }
  .caption-bc-back { left: 983px; top: 443px; font-size: 20px; }
  .caption-regular-env { left: 672px; top: 935px; font-size: 22px; }
</style>
</head>
<body>

  <div class="sheet env-large env-white">
    <svg class="flap" viewBox="0 0 408 72" height="72" preserveAspectRatio="none">
      <path d="M0,0 H408 V22 Q404,30 396,33 L214,69 Q204,72 194,69 L12,33 Q4,30 0,22 Z" fill="#fff" stroke="#9a9a9a" stroke-width="1"/>
    </svg>
    <div class="flap-content on-white" style="top:16px">
      <span class="mark"><i class="mark-dot"></i>Velcrest-Aura</span>
      <span class="flap-url" style="color:var(--navy)">www.velcrestaura.com</span>
    </div>
  </div>

  <div class="sheet env-large env-red">
    <svg class="flap" viewBox="0 0 408 72" height="72" preserveAspectRatio="none">
      <path d="M0,0 H408 V22 Q404,30 396,33 L214,69 Q204,72 194,69 L12,33 Q4,30 0,22 Z" fill="var(--red)"/>
    </svg>
    <div class="flap-content" style="top:16px">
      <span class="mark"><i class="mark-dot"></i>Velcrest-Aura</span>
      <span class="flap-url">www.velcrestaura.com</span>
    </div>
  </div>

  <div class="sheet env-large env-blue">
    <svg class="flap" viewBox="0 0 408 72" height="72" preserveAspectRatio="none">
      <path d="M0,0 H408 V22 Q404,30 396,33 L214,69 Q204,72 194,69 L12,33 Q4,30 0,22 Z" fill="var(--navy)"/>
    </svg>
    <div class="flap-content" style="top:16px">
      <span class="mark"><i class="mark-dot"></i>Velcrest-Aura</span>
      <span class="flap-url">www.velcrestaura.com</span>
    </div>
  </div>

  <div class="sheet letterhead">
    <div class="letterhead-head">
      <span class="mark"><i class="mark-dot"></i>Velcrest-Aura</span>
      <div class="tagline">Bringing Comfort To Every Day</div>
      <div class="address">Street Name, City, State, zip code</div>
    </div>
    <svg class="wave" viewBox="0 0 400 100" height="100" preserveAspectRatio="none">
      <path d="M0,76 C120,56 250,96 400,12 V100 H0 Z" fill="var(--navy)"/>
      <path d="M0,64 C120,44 250,84 400,0 V7 C250,92 120,52 0,70 Z" fill="var(--red)"/>
    </svg>
    <span class="web">www.velcrestaura.com</span>
  </div>
  <div class="caption caption-large-env">Envelope (13 1/2 X 18 1/2)</div>

  <div class="sheet card card-front">
    <div class="card-name">Your Name <span class="role">/ Title</span></div>
    <div class="brand">
      <span class="mark"><i class="mark-dot"></i>Velcrest-Aura</span>
      <div class="tagline">Bringing Comfort To Every Day</div>
    </div>
    <ul class="contacts">
      <li><svg viewBox="0 0 10 10"><path d="M2,0 L4,2 L3,4 Q5,6 6,7 L8,6 L10,8 L8,10 Q0,9 0,2 Z"/></svg>123-456-7890</li>
      <li><svg viewBox="0 0 10 10"><circle cx="5" cy="3" r="2.6"/><path d="M0,10 Q5,3 10,10 Z"/></svg>123-456-7890</li>
      <li><svg viewBox="0 0 10 10"><rect x="0" y="2" width="10" height="6"/></svg>hi@velcrestaura.com</li>
      <li><svg viewBox="0 0 10 10"><circle cx="5" cy="5" r="5"/></svg>www.velcrestaura.com</li>
    </ul>
    <svg class="wave" viewBox="0 0 400 100" height="80" preserveAspectRatio="none">
      <path d="M0,62 C120,48 250,82 400,14 V100 H0 Z" fill="var(--navy)"/>
      <path d="M0,50 C120,34 250,70 400,2 V10 C250,78 120,40 0,56 Z" fill="var(--red)"/>
    </svg>
    <span class="web">Street Name, City, State, zip code</span>
  </div>
  <div class="caption caption-bc-front">BC Front</div>

  <div class="sheet card card-back">
    <div class="brand">
      <span class="mark"><i class="mark-dot"></i>Velcrest-Aura</span>
      <div class="tagline">Bringing Comfort To Every Day</div>
    </div>
    <svg class="wave" viewBox="0 0 400 100" height="90" preserveAspectRatio="none">
      <path d="M0,20 C40,80 200,40 400,48 V100 H0 Z" fill="var(--navy)"/>
      <path d="M0,8 C40,70 200,28 400,36 V42 C200,36 40,76 0,14 Z" fill="var(--red)"/>
    </svg>
    <span class="web">www.velcrestaura.com</span>
  </div>
  <div class="caption caption-bc-back">BC Back</div>

  <div class="sheet env-regular-back">
    <svg class="flap" viewBox="0 0 571 96" height="96" preserveAspectRatio="none">
      <path d="M0,0 H571 V30 Q566,40 552,44 L300,93 Q286,96 272,93 L19,44 Q5,40 0,30 Z" fill="var(--navy)"/>
    </svg>
    <div class="flap-content" style="top:28px">
      <span class="mark"><i class="mark-dot"></i>Velcrest-Aura</span>
      <span class="flap-url">www.velcrestaura.com</span>
    </div>
  </div>

  <div class="sheet env-regular-front">
    <div class="brand">
      <span class="mark"><i class="mark-dot"></i>Velcrest-Aura</span>
      <div class="tagline">Bringing Comfort To Every Day</div>
      <div class="address">Street Name, City, State, zip code</div>
    </div>
    <svg class="wave" viewBox="0 0 400 100" height="110" preserveAspectRatio="none">
      <path d="M0,78 C110,54 250,100 400,16 V100 H0 Z" fill="var(--navy)"/>
      <path d="M0,66 C110,42 250,88 400,2 V9 C250,96 110,50 0,72 Z" fill="var(--red)"/>
    </svg>
    <span class="web">www.velcrestaura.com</span>
  </div>
  <div class="caption caption-regular-env">Regular&nbsp; Envelope</div>

</body>
</html>
```